Studying Effectively To Do List

I am looking to design a new "Study To Do List" for High School students (Ages 15 - 18) . This will be printed as an A4 notepad and so should only be a single A4 page.

The Design will need to be professional and look semi-serious but also be appealing to High school students (Ages 15 - 18) and should NOT be gender specific.

I have attached a word document outlining the structure of the page. The space provided should be large enough that people can write in it comfortably.

The notepad will most likely be printed in black and white but I'm also looking at coloured options - colours should be kept to a minimum.

This will be printed professionally and should also include a 3mm bleed.

The design should also include the business logo (included in the word document)

Target Market(s)

High School students (Ages 15 - 18). Both genders

Industry/Entity Type

Education

Font styles to use
Serif
Sans Serif

Requirements
Must have
• Please see the word document attached.
Should not have
• Too much colour

```html
<!DOCTYPE html>
<html lang="en">
<head>
<meta charset="utf-8">
<title>Study To Do List</title>
<link rel="stylesheet" href="https://fonts.googleapis.com/css2?family=Ubuntu:wght@400;500;700&display=swap">
<style>
  :root {
    --backdrop: #e4e4e4;
    --paper: #ffffff;
    --accent: #e8541e;
    --ink: #1f2f3d;
  }
  * { box-sizing: border-box; margin: 0; padding: 0; }
  html, body { width: 1200px; height: 1001px; overflow: hidden; }
  body {
    background: var(--backdrop);
    font-family: "Ubuntu", sans-serif;
    position: relative;
  }
  .sheet {
    position: absolute;
    left: 260px; top: 20px;
    width: 680px; height: 962px;
    background: var(--paper);
    box-shadow: 0 2px 10px rgba(0,0,0,0.12);
  }
  .brand {
    position: absolute; left: 60px; top: 70px;
    display: flex; align-items: center; gap: 12px;
  }
  .brand-dot {
    width: 34px; height: 34px; border-radius: 50%;
    background: var(--accent);
  }
  .brand-name {
    font-size: 30px; font-weight: 700; color: var(--ink);
  }
  .date-label {
    position: absolute; left: 355px; top: 42px;
    font-size: 13px; font-weight: 700; color: var(--ink); letter-spacing: 1px;
  }
  .grid-table {
    position: absolute;
    border-collapse: collapse;
    table-layout: fixed;
  }
  .grid-table th, .grid-table td {
    border: 1px solid var(--accent);
  }
  .grid-table th {
    font-size: 13px; font-weight: 700; color: var(--ink);
    letter-spacing: 1.5px; height: 30px;
  }
  .revision-table { left: 355px; top: 70px; width: 285px; }
  .revision-table td { height: 27px; }
  .review-table { left: 40px; top: 790px; width: 600px; }
  .review-table td { height: 37px; }
  .section-title {
    position: absolute;
    font-size: 13px; font-weight: 700; color: var(--ink); letter-spacing: 1.5px;
  }
  .homework-title { left: 55px; top: 228px; }
  .assessments-title { left: 355px; top: 252px; }
  .entry-list { position: absolute; list-style: none; }
  .homework-list { left: 55px; top: 262px; width: 260px; }
  .assessment-list { left: 355px; top: 284px; width: 285px; }
  .entry { height: 82px; }
  .field {
    display: flex; align-items: flex-end;
    font-size: 11px; color: var(--accent);
    height: 17px;
  }
  .homework-list .field { height: 24px; }
  .field-line {
    flex: 1; margin-left: 4px;
    border-bottom: 1px solid var(--accent);
    height: 1px; margin-bottom: 2px;
  }
  .blank-line {
    border-bottom: 1px solid var(--accent);
    height: 26px;
  }
</style>
</head>
<body>
  <main class="sheet">
    <div class="brand">
      <span class="brand-dot"></span>
      <span class="brand-name">Brightway</span>
    </div>

    <div class="date-label">Date:</div>

    <table class="grid-table revision-table">
      <tr><th colspan="2">REVISION</th></tr>
      <tr><td></td><td></td></tr>
      <tr><td></td><td></td></tr>
      <tr><td></td><td></td></tr>
    </table>

    <h2 class="section-title homework-title">HOMEWORK</h2>
    <ul class="entry-list homework-list">
      <li class="entry"><div class="field">Subject:<span class="field-line"></span></div><div class="field">Task:<span class="field-line"></span></div></li>
      <li class="entry"><div class="field">Subject:<span class="field-line"></span></div><div class="field">Task:<span class="field-line"></span></div></li>
      <li class="entry"><div class="field">Subject:<span class="field-line"></span></div><div class="field">Task:<span class="field-line"></span></div></li>
      <li class="entry"><div class="field">Subject:<span class="field-line"></span></div><div class="field">Task:<span class="field-line"></span></div></li>
      <li class="entry"><div class="field">Subject:<span class="field-line"></span></div><div class="field">Task:<span class="field-line"></span></div></li>
      <li class="entry"><div class="field">Subject:<span class="field-line"></span></div><div class="field">Task:<span class="field-line"></span></div></li>
    </ul>

    <h2 class="section-title assessments-title">ASSESSMENTS</h2>
    <ul class="entry-list assessment-list">
      <li class="entry"><div class="field">Assessment:<span class="field-line"></span></div><div class="field">Due:<span class="field-line"></span></div><div class="field">Element:</div><div class="blank-line"></div></li>
      <li class="entry"><div class="field">Assessment:<span class="field-line"></span></div><div class="field">Due:<span class="field-line"></span></div><div class="field">Element:</div><div class="blank-line"></div></li>
      <li class="entry"><div class="field">Assessment:<span class="field-line"></span></div><div class="field">Due:<span class="field-line"></span></div><div class="field">Element:</div><div class="blank-line"></div></li>
      <li class="entry"><div class="field">Assessment:<span class="field-line"></span></div><div class="field">Due:<span class="field-line"></span></div><div class="field">Element:</div><div class="blank-line"></div></li>
      <li class="entry"><div class="field">Assessment:<span class="field-line"></span></div><div class="field">Due:<span class="field-line"></span></div><div class="field">Element:</div><div class="blank-line"></div></li>
      <li class="entry"><div class="field">Assessment:<span class="field-line"></span></div><div class="field">Due:<span class="field-line"></span></div><div class="field">Element:</div><div class="blank-line"></div></li>
    </ul>

    <table class="grid-table review-table">
      <colgroup><col style="width:150px"><col style="width:150px"><col style="width:300px"></colgroup>
      <tr><th colspan="2">NOTES</th><th>PRACTICE</th></tr>
      <tr><td></td><td></td><td></td></tr>
      <tr><td></td><td></td><td></td></tr>
      <tr><td></td><td></td><td></td></tr>
    </table>
  </main>
</body>
</html>
```